Baby Shower Invitation for Vectored Image Provided

Caroline & Desmond's Baby Shower - Black/White/Gold Colors preferred
Please use the vectored portrait image attached. I'd like us on the lower right side of the invitation.
Can be horizontal or vertical layout.
The second image attached has the information needed for you to complete.
I don't want that style copied, it is just an example.

```html
<!DOCTYPE html>
<html lang="en">
<head>
<meta charset="utf-8">
<title>Caroline's Baby Shower Invitation</title>
<link rel="stylesheet" href="https://fonts.googleapis.com/css2?family=Cardo:wght@400;700&display=swap">
<style>
  :root {
    --ink-dark: #1b1b1b;
    --ink-mid: #3a3a3a;
    --gold: #d9c24f;
    --gold-deep: #c4a32a;
    --gold-light: #ecd965;
    --band-text: #2a2414;
    --white: #ffffff;
    --frame: #ffffff;
  }
  * { margin: 0; padding: 0; box-sizing: border-box; }
  html, body { width: 848px; height: 1200px; overflow: hidden; background: var(--frame); }
  .invitation {
    position: absolute; left: 4px; top: 4px; width: 840px; height: 1192px;
    background: radial-gradient(ellipse at 50% 40%, var(--ink-mid) 0%, #262626 55%, var(--ink-dark) 100%);
    font-family: "Cardo", Georgia, serif;
    color: var(--white);
    overflow: hidden;
  }
  .line { position: absolute; left: 0; width: 100%; text-align: center; white-space: nowrap; line-height: 1; }
  .headline { top: 128px; font-size: 118px; font-weight: 400; letter-spacing: 1px; }
  .subhead { color: var(--gold); font-size: 56px; }
  .subhead.first { top: 270px; }
  .subhead.second { top: 342px; }
  .invite-copy { font-size: 29px; }
  .invite-copy.first { top: 424px; }
  .invite-copy.second { top: 461px; }
  .guest-name { top: 530px; font-size: 50px; font-weight: 700; color: var(--gold); }

  .details { position: absolute; left: 151px; top: 604px; width: 537px; height: 181px; }
  .details svg { position: absolute; inset: 0; }
  .date-day { position: absolute; left: 0; width: 296px; top: 24px; text-align: center; font-size: 48px; line-height: 1; }
  .date-num { position: absolute; left: 0; width: 296px; top: 80px; text-align: center; font-size: 68px; font-weight: 700; color: var(--gold); line-height: 1; }
  .date-num sup { font-size: 30px; vertical-align: 28px; margin-right: 10px; }
  .time { position: absolute; left: 318px; top: 15px; font-size: 27px; line-height: 1; }
  .venue { position: absolute; left: 318px; top: 68px; font-size: 27px; line-height: 36px; }

  .rsvp-band {
    position: absolute; left: 0; top: 830px; width: 100%; height: 181px;
    background: linear-gradient(100deg, var(--gold-deep) 0%, var(--gold-light) 45%, var(--gold) 75%, var(--gold-deep) 100%);
  }
  .rsvp { position: absolute; left: 60px; width: 440px; text-align: center; color: var(--band-text); font-size: 30px; line-height: 1; white-space: nowrap; }
  .rsvp.title { top: 34px; }
  .rsvp.contact { top: 74px; }
  .rsvp.contact strong { font-weight: 700; }
  .rsvp.deadline { top: 114px; }

  .registry { position: absolute; left: 60px; width: 440px; text-align: center; font-size: 33px; line-height: 1; white-space: nowrap; }
  .registry.first { top: 1040px; }
  .registry.second { top: 1084px; }

  .couple-portrait {
    position: absolute; left: 530px; top: 830px; width: 245px; height: 325px;
    border-radius: 110px 110px 12px 12px;
    background: linear-gradient(180deg, #4a3a30 0%, #2a2624 45%, #1e1e1e 100%);
  }
</style>
</head>
<body>
  <main class="invitation">
    <h1 class="line headline">OH BOY !</h1>
    <p class="line subhead first">A LITTLE MAN</p>
    <p class="line subhead second">IS ON THE WAY!</p>
    <p class="line invite-copy first">Please join us for a</p>
    <p class="line invite-copy second">Baby Shower honoring</p>
    <h2 class="line guest-name">Caroline Whitmore</h2>

    <section class="details">
      <svg width="537" height="181" viewBox="0 0 537 181" aria-hidden="true">
        <g stroke="#d9c24f" stroke-width="1.5" stroke-dasharray="3 4" fill="none">
          <line x1="0" y1="1" x2="537" y2="1"/>
          <line x1="0" y1="180" x2="537" y2="180"/>
          <line x1="298" y1="1" x2="298" y2="180"/>
          <line x1="298" y1="52" x2="537" y2="52"/>
        </g>
      </svg>
      <p class="date-day">Saturday</p>
      <p class="date-num">1<sup>st</sup>Sept</p>
      <p class="time">11:30am-2:30pm</p>
      <p class="venue">The Ashgrove<br>1487 Fenwick St.<br>Raleigh, NC</p>
    </section>

    <section class="rsvp-band">
      <p class="rsvp title">RSVP TO</p>
      <p class="rsvp contact"><strong>Desmond at 919-555-0148</strong></p>
      <p class="rsvp deadline">by August 20th</p>
    </section>

    <p class="registry first">Caroline is registered at</p>
    <p class="registry second">Little Nest Baby</p>

    <div class="couple-portrait" role="img" aria-label="Illustrated portrait of the expecting couple"></div>
  </main>
</body>
</html>
```